Tech Startup Needs Business Card Design

I am looking for an eye catching business card design for our new company, Torn Kite. We are a place for business owners and contractors to share their experiences with their customers and check their current customers. Our website, www.torn-kite.co, may be able to offer some guidance as to the design.

Industry/Entity Type

Business

Contact Information for Business Card

Owen Barthwick
888-417-3083
Owen@torn-kite.co
www.torn-kite.co

```html
<!DOCTYPE html>
<html lang="en">
<head>
<meta charset="utf-8">
<title>Torn Kite – Business Card</title>
<link rel="stylesheet" href="https://fonts.googleapis.com/css2?family=Open+Sans:wght@400;600;700&display=swap">
<style>
  :root {
    --backdrop: #e9e6e1;
    --card-black: #050505;
    --card-white: #f2f2f2;
    --brand-red: #e3232f;
    --ink-dark: #111111;
    --ink-light: #ffffff;
    --ghost-mark: #261d1a;
    --leaf-green: #2f9a3a;
  }
  * { box-sizing: border-box; margin: 0; padding: 0; }
  html, body {
    width: 1200px; height: 780px; overflow: hidden;
    background: var(--backdrop);
    font-family: "Open Sans", Arial, sans-serif;
  }
  .stage {
    width: 1200px; height: 780px;
    display: flex; align-items: center; justify-content: center; gap: 60px;
  }
  .card {
    position: relative;
    width: 520px; height: 300px;
    border-radius: 18px;
    overflow: hidden;
    background: var(--card-black);
    box-shadow: 0 10px 26px rgba(0,0,0,.22);
  }

  /* Front */
  .card-front__top {
    position: absolute; left: 0; top: 0; right: 0; height: 128px;
    background: var(--card-white);
    display: flex; align-items: center; padding-left: 44px; gap: 14px;
  }
  .brand-dot {
    width: 34px; height: 34px; border-radius: 50%;
    background: var(--brand-red); flex: none;
  }
  .brand-name {
    font-weight: 700; font-size: 58px; letter-spacing: -1px;
    line-height: 1; color: var(--ink-dark);
  }
  .card-front__stripe {
    position: absolute; left: 0; right: 0; top: 128px; height: 28px;
    background: var(--brand-red);
  }
  .holder-name {
    position: absolute; top: 130px; left: 230px;
    font-weight: 700; font-size: 17px; color: var(--ink-light);
    line-height: 24px;
  }
  .contact {
    position: absolute; top: 182px; left: 268px;
    font-size: 14px; line-height: 21px; color: var(--ink-light);
    list-style: none;
  }
  .contact__label { color: var(--brand-red); font-weight: 700; margin-right: 4px; }
  .contact__web { color: var(--brand-red); padding-left: 22px; }

  /* Back */
  .ghost-mark {
    position: absolute; left: 150px; top: 40px;
    width: 220px; height: 220px; border-radius: 50%;
    background: var(--ghost-mark);
  }
  .card-back__brand {
    position: absolute; inset: 0;
    display: flex; align-items: center; justify-content: center; gap: 14px;
  }
  .card-back__brand .brand-name { color: var(--ink-light); font-size: 60px; }
</style>
</head>
<body>
<main class="stage">
  <section class="card card-front" aria-label="Business card front">
    <div class="card-front__top">
      <span class="brand-dot"></span>
      <span class="brand-name">Torn Kite</span>
    </div>
    <div class="card-front__stripe"></div>
    <p class="holder-name">Owen Barthwick</p>
    <ul class="contact">
      <li><span class="contact__label">P:</span>888-417-3083</li>
      <li><span class="contact__label">E:</span>Owen@torn-kite.co</li>
      <li class="contact__web">www.torn-kite.co</li>
    </ul>
  </section>

  <section class="card card-back" aria-label="Business card back">
    <div class="ghost-mark"></div>
    <div class="card-back__brand">
      <span class="brand-dot"></span>
      <span class="brand-name">Torn Kite</span>
    </div>
  </section>
</main>
</body>
</html>
```